Yoga Mat Package Design

We need a package designed for a Yoga Mat. The design will consist of a paper insert 38*12cm in size, that will wrap around the Yoga Mat.

Full package details are attached.

Target Market(s)

Female.
Consumers.

Requirements
Must have
• See attached project brief
Nice to have

```html
<!DOCTYPE html>
<html lang="en">
<head>
<meta charset="utf-8">
<title>True Asana – Go Everywhere Mat Wrap</title>
<link href="https://fonts.googleapis.com/css2?family=Arimo:ital,wght@0,400;0,700;1,700&family=Raleway:wght@300;400;700&display=swap" rel="stylesheet">
<style>
  :root {
    --brand-blue: #55afd3;
    --logo-blue: #1b78c9;
    --brand-green: #84c51f;
    --ink: #1d1d1d;
    --paper: #ffffff;
    --edge: #cfcfcf;
  }
  * { margin: 0; padding: 0; box-sizing: border-box; }
  html, body { width: 1200px; height: 1200px; overflow: hidden; background: var(--paper); }
  .canvas { position: relative; width: 1200px; height: 1200px; }

  .wrap {
    position: absolute; left: 23px; top: 262px; width: 1150px; height: 362px;
    background: var(--paper); border-top: 1px solid var(--edge); border-bottom: 1px solid var(--edge);
    overflow: hidden;
  }
  .band { position: absolute; top: 0; bottom: 0; width: 27px; }
  .band--left { left: 0; background: var(--brand-blue); }
  .band--right { right: 0; background: var(--brand-green); }

  .hero-photo {
    position: absolute; left: 27px; top: 0; width: 658px; height: 362px;
    background:
      linear-gradient(to right, rgba(255,255,255,0) 80%, #fff 100%),
      linear-gradient(to bottom, #ffffff 0%, #f6f6f7 72%, #e4e4e6 80%, #eceded 100%);
  }
  .hero-photo::after {
    content: ""; position: absolute; left: 0; top: 322px; width: 640px; height: 14px;
    background: linear-gradient(to right, #f04fb9, #f58fd2 85%, rgba(255,255,255,0));
  }

  .brand { position: absolute; left: 250px; top: 0; width: 460px; text-align: center; font-family: "Raleway", sans-serif; }
  .brand__mark {
    position: absolute; left: 211px; top: 30px; width: 40px; height: 40px; border-radius: 50%;
    background: var(--brand-green);
  }
  .brand__name {
    position: absolute; left: 0; right: 0; top: 114px;
    font-weight: 700; font-size: 40px; letter-spacing: 0.5px; color: var(--logo-blue);
  }
  .brand__product {
    position: absolute; left: 0; right: 0; top: 162px;
    font-weight: 400; font-size: 22px; color: var(--brand-green);
  }
  .brand__tagline {
    position: absolute; left: 0; right: 0; top: 191px;
    font-weight: 300; font-size: 19px; color: var(--brand-blue); white-space: nowrap;
  }

  .thickness-badge {
    position: absolute; left: 621px; top: 232px; width: 56px; height: 56px; border-radius: 50%;
    background: var(--brand-green); color: #fff; font-family: "Arimo", sans-serif;
    font-size: 17px; line-height: 19px; text-align: center; padding-top: 9px;
  }

  .info { position: absolute; left: 745px; top: 0; width: 380px; font-family: "Arimo", sans-serif; color: var(--ink); }
  .info__heading {
    position: absolute; left: 0; font-weight: 400; font-size: 26px; color: var(--brand-blue); white-space: nowrap;
  }
  .features { position: absolute; left: 3px; top: 62px; list-style: none; font-size: 9.4px; line-height: 13.3px; }
  .features li { position: relative; padding-left: 14px; white-space: nowrap; }
  .features li::before {
    content: ""; position: absolute; left: 1px; top: 4px; width: 6px; height: 6px; border-radius: 50%;
    background: var(--brand-green);
  }
  .tips { position: absolute; left: 8px; width: 355px; font-size: 7.8px; line-height: 9.8px; }
  .tips p { margin: 0; }
</style>
</head>
<body>
<div class="canvas">
  <section class="wrap">
    <div class="band band--left"></div>
    <div class="hero-photo" role="img" aria-label="Photo of a woman in upward-facing dog pose on a pink yoga mat"></div>

    <div class="brand">
      <div class="brand__mark"></div>
      <div class="brand__name">TRUE ASANA</div>
      <div class="brand__product">Go Everywhere Mat</div>
      <div class="brand__tagline">A premium, foldable yoga mat for yoga everywhere</div>
    </div>

    <div class="thickness-badge">1.5<br>mm</div>

    <div class="info">
      <h2 class="info__heading" style="top:28px;">MAT FEATURES</h2>
      <ul class="features">
        <li>Folds easily to fit in small bags, backpacks, and suitcases</li>
        <li>Made of 100% natural tree rubber</li>
        <li>71" long 26" wide Yoga mat ensures comfort for Yogis of all shapes and sizes</li>
        <li>Two-sided surface allows for a non-slip surface that grips the floor</li>
        <li>Tightly woven top surface offers superior grip protection, for all types of Yoga</li>
      </ul>

      <h2 class="info__heading" style="top:153px;">Go Everywhere Mat Use Tips</h2>
      <div class="tips" style="top:183px;">
        <p>The Go Everywhere Mat by True Asana is thin at only at approximately <b>1.5mm.</b> While you'll be able have a complete practice on the mat, there are some poses that may not feel comfortable with this level of thickness, <b><i>e.g. headstands or poses such as camel or low lounge where a lot of weight is on your knees.</i></b> Adjust your practice as necessary.</p>
        <p>Add a towel underneath for additional protection against hard surfaces</p>
        <p>The Go Everywhere Mat can be used as a layer over another yoga mat</p>
      </div>

      <h2 class="info__heading" style="top:258px;">Go Everywhere Mat Care Tips</h2>
      <div class="tips" style="top:289px;">
        <p>Sensitive to natural rubber smell? It will go away with use. But to accelerate the process hang the mat in a well ventilated area but not in direct sunlight.</p>
        <p>Clean your mat with a mild soapy rag and rub gently, then with a damp rag rinse it off well.</p>
        <p>If wet, from sweat or wash, allow the mat to hang dry before rolling.</p>
        <p>Do not wash your mat in the washing machine.</p>
        <p>Do not store your mat in direct natural sunlight.</p>
      </div>
    </div>

    <div class="band band--right"></div>
  </section>
</div>
</body>
</html>
```